HOME IMPROVEMENT Business Card

I want a very unique business card. nothing typical and boring. Im open to you ideas. Ive seen cards with gold and silver or color foil and spot UV coatings. Im looking for something that looks cool and grabs attention. I like rounded corners but am open to all suggestions. We are a home improvement company and I will have a presentation folder printed and a catalog printed also and want to keep that same theme. I love the colors in our logo but I am open at looking at a 3rd color that would work with my logo. I hope that helps.
Card should include
Address
Phone
Fax
Email
Website
Target Market(s)
Home owners, people looking to remodel their home
Industry/Entity Type
Home Improvement
Contact Information for Business Card
2873 Maple Crest Avenue Unit 410
Linden Falls, Il 60284
Phone
Direct Line
Email
Website
Font styles to use
Other font styles liked:
- IM OPEN MINDED
Requirements
Must have
- High end quality look nothing boring I like rounded corners but am open minded
Nice to have
- WOW. I want something nice and impressive.
Should not have
- ??? Not sure

```html
<!DOCTYPE html>
<html lang="en">
<head>
<meta charset="utf-8">
<title>Hearthline Business Card</title>
<link rel="stylesheet" href="https://fonts.googleapis.com/css2?family=Open+Sans:wght@400;600;800&display=swap">
<style>
  :root {
    --navy: #1b1f4f;
    --green: #0f9a44;
    --bar-grey: #e4e4e4;
    --paper: #ffffff;
    --backdrop: #c6c6c6;
    --ink: #1e1e2a;
  }
  html, body {
    margin: 0;
    width: 1200px;
    height: 1200px;
    overflow: hidden;
    background: var(--backdrop);
    font-family: "Open Sans", Arial, sans-serif;
  }
  .sheet {
    width: 1200px;
    height: 1200px;
    display: flex;
    align-items: center;
    justify-content: center;
    gap: 50px;
  }
  .card {
    position: relative;
    width: 540px;
    height: 363px;
    background: var(--paper);
    overflow: hidden;
    box-shadow: 0 2px 6px rgba(0,0,0,0.12);
  }
  .card svg.art {
    position: absolute;
    inset: 0;
  }
  .brand {
    position: absolute;
    display: flex;
    align-items: center;
    gap: 8px;
    color: var(--navy);
    font-weight: 800;
    font-size: 32px;
    letter-spacing: -0.5px;
    line-height: 1;
    white-space: nowrap;
  }
  .brand-mark {
    width: 13px;
    height: 13px;
    background: var(--green);
  }
  .card-front .brand { left: 298px; top: 86px; }
  .card-back .brand { left: 50%; top: 50%; transform: translate(-50%, -50%); font-size: 36px; }
  .card-back .brand-mark { width: 15px; height: 15px; }
  .address {
    position: absolute;
    left: 66px;
    top: 182px;
    margin: 0;
    font-size: 11.5px;
    line-height: 16px;
    color: var(--ink);
    font-style: normal;
  }
  .contact-list {
    position: absolute;
    left: 44px;
    top: 224px;
    margin: 0;
    padding: 0;
    list-style: none;
    font-size: 11.5px;
    color: var(--ink);
  }
  .contact-list li {
    display: flex;
    align-items: center;
    height: 17px;
  }
  .contact-icon { width: 12px; height: 12px; margin-right: 10px; }
  .contact-label { width: 70px; }
</style>
</head>
<body>
<main class="sheet">
  <section class="card card-front" aria-label="Business card front">
    <svg class="art" width="540" height="363" viewBox="0 0 540 363">
      <line x1="0" y1="80" x2="290" y2="80" stroke="var(--green)" stroke-width="2"/>
      <polyline points="0,316 380,316 416,294 452,316 540,316" fill="none" stroke="var(--navy)" stroke-width="5"/>
      <polyline points="0,332 380,332 416,308 452,332 540,332" fill="none" stroke="var(--green)" stroke-width="2.5"/>
    </svg>
    <div class="brand"><span class="brand-mark"></span>Hearthline</div>
    <address class="address">2873 Maple Crest Avenue Unit 410<br>Linden Falls, Il 60284</address>
    <ul class="contact-list">
      <li>
        <svg class="contact-icon" viewBox="0 0 14 14"><circle cx="7" cy="7" r="6.2" fill="none" stroke="var(--navy)" stroke-width="1.2"/><rect x="5" y="3.5" width="4" height="7" rx="0.8" fill="var(--navy)"/></svg>
        <span class="contact-label">Phone</span><span>: 012 555 0193</span>
      </li>
      <li>
        <svg class="contact-icon" viewBox="0 0 14 14"><circle cx="7" cy="7" r="6.2" fill="none" stroke="var(--navy)" stroke-width="1.2"/><path d="M4.5 4 L6 4 L6.6 5.8 L5.8 6.5 Q6.6 8 7.8 8.5 L8.5 7.7 L10 8.3 L10 9.8 Q6 10 4.5 5.5 Z" fill="var(--navy)"/></svg>
        <span class="contact-label">Direct Line</span><span>: 0123 789</span>
      </li>
      <li>
        <svg class="contact-icon" viewBox="0 0 14 14"><circle cx="7" cy="7" r="6.2" fill="none" stroke="var(--navy)" stroke-width="1.2"/><rect x="3.8" y="4.8" width="6.4" height="4.4" fill="var(--navy)"/><polyline points="3.8,4.8 7,7.3 10.2,4.8" fill="none" stroke="#fff" stroke-width="0.8"/></svg>
        <span class="contact-label">Email</span><span>: info@hearthline.com</span>
      </li>
      <li>
        <svg class="contact-icon" viewBox="0 0 14 14"><circle cx="7" cy="7" r="6.2" fill="none" stroke="var(--navy)" stroke-width="1.2"/><circle cx="7" cy="7" r="3.4" fill="none" stroke="var(--navy)" stroke-width="1"/><line x1="3.6" y1="7" x2="10.4" y2="7" stroke="var(--navy)" stroke-width="0.8"/><ellipse cx="7" cy="7" rx="1.4" ry="3.4" fill="none" stroke="var(--navy)" stroke-width="0.8"/></svg>
        <span class="contact-label">Website</span><span>: www.hearthline.com</span>
      </li>
    </ul>
  </section>

  <section class="card card-back" aria-label="Business card back">
    <svg class="art" width="540" height="363" viewBox="0 0 540 363">
      <polygon points="0,0 186,0 0,101" fill="var(--green)"/>
      <polygon points="540,269 540,363 436,363" fill="var(--navy)"/>
      <g fill="var(--bar-grey)" transform="rotate(-33 270 181)">
        <rect x="150" y="112" width="270" height="13"/>
        <rect x="120" y="142" width="300" height="13"/>
        <rect x="130" y="208" width="290" height="13"/>
        <rect x="110" y="238" width="260" height="13"/>
        <rect x="170" y="268" width="180" height="13"/>
      </g>
    </svg>
    <div class="brand"><span class="brand-mark"></span>Hearthline</div>
  </section>
</main>
</body>
</html>
```